Web design project for exciting Australian start-up

Background
We are looking for a creative and talented web design artist to work alongside our market leading web developer.
• You will be required to create a modern and clean design theme for our website, incorporating selected rustic colour scheme elements for our exciting Australian start-up to operate within the coffee industry.
reoccurring work to be expected to flow to the successful designer.
Requirements
• c. 5 - 10 page website
• Landing page
• Log in/ out
• 404 template
• Typography is emphasised
• Please use either a) quillnest.com, b) free web fonts, c) plovra fonts
• All design elements in vector format
• Preferably with icons for each header title(i.e. about us, how it works etc) but designer have free reign over how the site looks, so might not be applicable
• All pages to be responsive
• Down to Kelvo resolution

High level visual design brief attached - additional pages to be worked from base design.

Design inspiration
• We would like to use design elements from the following sources:
http://www.plovra.com/vintel/ (Functionality)
Colour scheme refer to logo and complementary style guide

```html
<!DOCTYPE html>
<html lang="en">
<head>
<meta charset="utf-8">
<title>Brewline – Marketplace</title>
<link rel="stylesheet" href="https://fonts.googleapis.com/css2?family=Roboto:wght@300;400;700;900&family=Cabin:wght@400;700&display=swap">
<style>
:root{
  --orange:#f7941d;
  --ink:#333;
  --muted:#777;
  --line:#dcdcdc;
  --chip:#efefef;
  --chip-dark:#d9d9d9;
  --star-off:#d6d6d6;
  --footer-bg:#f2f2f2;
}
*{box-sizing:border-box;margin:0;padding:0}
html,body{width:1163px;height:1200px;overflow:hidden;background:#fff}
body{position:relative;font-family:"Roboto",sans-serif;font-weight:300;color:var(--ink)}
.abs{position:absolute}

/* header */
.brand{left:44px;top:34px;display:flex;align-items:center;gap:10px;font-family:"Roboto",sans-serif;font-weight:900;font-size:26px;letter-spacing:1px;color:#222}
.brand-mark{width:22px;height:22px;border-radius:50%;background:var(--orange)}
.account-nav{top:39px;height:30px;display:flex;font-size:13px}
.nav-btn{border:1px solid #333;height:30px;display:flex;align-items:center;justify-content:center;color:var(--orange)}
.nav-btn.logout{color:#222}
.header-rule{left:0;top:106px;width:1163px;height:3px;background:var(--orange)}

/* filters */
.page-title{left:45px;top:127px;font-size:26px}
.chip{height:30px;display:flex;align-items:center;padding-left:12px;background:var(--chip);font-size:16px;font-weight:400;color:#444}
.chip.active{background:var(--chip-dark)}
.toolbar{top:228px;font-size:15px;color:var(--muted)}
.select{top:226px;height:25px;border:1px solid var(--line);display:flex;align-items:center;justify-content:space-between;padding:0 8px;font-size:15px;color:var(--muted)}
.caret{width:0;height:0;border-left:5px solid transparent;border-right:5px solid transparent;border-top:6px solid var(--orange)}
.rule{height:1px;background:var(--line)}
.section-title{left:46px;top:273px;font-size:25px}

/* result card */
.card{left:40px;width:1086px;height:184px;border:1px solid var(--line)}
.supplier-logo{left:12px;top:12px;width:149px;height:155px;border:1px solid #ccc;display:flex;align-items:center;justify-content:center;gap:6px;font-weight:700;font-size:17px}
.supplier-logo .dot{width:14px;height:14px;background:var(--ink)}
.bean-name{left:185px;top:16px;font-size:17px;color:var(--orange);font-weight:400;width:214px;padding-bottom:6px;border-bottom:1px solid var(--line)}
.blend{left:185px;top:56px;font-size:16px}
.attr{left:185px;width:214px;height:29px;background:var(--chip);padding-left:30px;display:flex;align-items:center;font-size:16px}
.reviews{left:786px;top:12px;width:280px}
.reviews-head{display:flex;align-items:center;gap:12px;font-size:21px;height:40px;border-bottom:1px solid var(--line);padding-bottom:6px;color:#444}
.rating{display:flex;align-items:center;gap:22px;height:68px;border-bottom:1px solid var(--line);font-size:15.5px;line-height:21px;color:#555}
.stars{display:flex;gap:2px}
.offerings{display:flex;align-items:center;gap:26px;height:40px;font-size:16px;color:#555}
.offer-icons{display:flex;gap:10px}

/* footer */
.footer-rule{left:25px;top:751px;width:1122px;height:1px;background:var(--line)}
.col{top:792px;width:200px;text-align:center;font-family:"Cabin",sans-serif}
.col-photo{width:104px;height:104px;border-radius:50%;margin:0 auto}
.col h3{font-size:21px;font-weight:700;margin-top:20px;color:#222}
.col ul{list-style:none;width:136px;margin:16px auto 0}
.col li{height:33px;display:flex;align-items:center;justify-content:center;gap:8px;border-bottom:1px solid #eee;font-size:14px;color:var(--muted)}
.col li .caret{border-top-width:6px}
.social li{justify-content:flex-start;gap:20px;height:37px}
.social .icon{width:26px;height:26px;border-radius:50%;background:var(--orange)}
.col-divider{top:850px;width:2px;height:240px;background:linear-gradient(#fff,#ddd,#fff)}
.copyright-bar{left:0;top:1157px;width:1163px;height:43px;background:var(--footer-bg);border-top:1px solid #e3e3e3}
.copyright{left:105px;top:1172px;font-size:10px;font-weight:400;color:#555}
</style>
</head>
<body>

<header>
  <div class="abs brand"><span class="brand-mark"></span>BREWLINE</div>
  <nav class="abs account-nav" style="left:809px">
    <a class="nav-btn" style="width:124px">My Account</a>
  </nav>
  <nav class="abs account-nav" style="left:944px">
    <a class="nav-btn" style="width:97px">Logged in</a>
    <a class="nav-btn logout" style="width:90px;border-left:none">Logout</a>
  </nav>
  <div class="abs header-rule"></div>
</header>

<main>
  <h1 class="abs page-title" style="font-weight:300">Marketplace</h1>

  <div class="abs chip" style="left:44px;top:170px;width:134px">Tender format</div>
  <div class="abs chip active" style="left:184px;top:170px;width:106px">All</div>
  <div class="abs chip" style="left:296px;top:170px;width:109px">One-off</div>
  <div class="abs chip" style="left:412px;top:170px;width:109px">Recurring</div>
  <div class="abs chip" style="left:874px;top:170px;width:116px">Quantity (kg)</div>
  <div class="abs chip active" style="left:1002px;top:170px;width:122px">35 kg/week</div>

  <div class="abs toolbar" style="left:46px">[X] results for Café Marlow</div>
  <div class="abs toolbar" style="left:289px;display:flex;align-items:center;gap:8px">
    <svg width="18" height="18" viewBox="0 0 24 24"><path fill="#f7941d" d="M12 2l3 7h7l-5.6 4.3 2.1 7.2L12 16.3 5.5 20.5l2.1-7.2L2 9h7z"/></svg>
    Save search
  </div>
  <div class="abs toolbar" style="left:845px">Sort</div>
  <div class="abs select" style="left:889px;width:137px">Highest rated <span class="caret"></span></div>
  <div class="abs select" style="left:1034px;width:91px">View
    <svg width="16" height="16" viewBox="0 0 16 16"><rect width="7" height="7" fill="#f7941d"/><rect x="9" width="7" height="7" fill="#f7941d"/><rect y="9" width="7" height="7" fill="#f7941d"/><rect x="9" y="9" width="7" height="7" fill="#f7941d"/></svg>
    <span class="caret"></span></div>
  <div class="abs rule" style="left:40px;top:257px;width:1086px"></div>

  <h2 class="abs section-title" style="font-weight:300">Results</h2>
  <div class="abs rule" style="left:40px;top:311px;width:1086px"></div>

  <!-- result 1 -->
  <article class="abs card" style="top:330px">
    <div class="abs supplier-logo" style="color:#5a2a14"><span class="dot" style="background:#5a2a14"></span>Ember Roast</div>
    <h3 class="abs bean-name">Coffee bean XX</h3>
    <p class="abs blend">Blend description:</p>
    <div class="abs attr" style="top:83px">Origin [xx]</div>
    <div class="abs attr" style="top:116px">Grind availability [xx]</div>
    <section class="abs reviews">
      <div class="reviews-head">
        <svg width="34" height="30" viewBox="0 0 34 30"><path d="M17 2C8 2 2 7 2 13s6 11 15 11c2 0 3 0 5-1l8 4-2-6c2-2 4-5 4-8C32 7 26 2 17 2z" fill="none" stroke="#f7941d" stroke-width="2"/></svg>
        Reviews for this bean
      </div>
      <div class="rating">
        <div class="stars">
          <svg width="116" height="22" viewBox="0 0 116 22"><g id="s"><path fill="#f7941d" d="M11 1l3 7h7l-5.6 4.3 2.1 7.2L11 15.3 4.5 19.5l2.1-7.2L1 8h7z"/></g><use href="#s" x="23"/><use href="#s" x="46"/><path transform="translate(69 0)" fill="#d6d6d6" d="M11 1l3 7h7l-5.6 4.3 2.1 7.2L11 15.3 4.5 19.5l2.1-7.2L1 8h7z"/><path transform="translate(92 0)" fill="#d6d6d6" d="M11 1l3 7h7l-5.6 4.3 2.1 7.2L11 15.3 4.5 19.5l2.1-7.2L1 8h7z"/></svg>
        </div>
        <span>Wholesaler's overall<br>customer rating</span>
      </div>
      <div class="offerings">
        <svg class="offer-icons" width="112" height="18" viewBox="0 0 112 18"><g fill="#f7941d"><rect x="2" y="4" width="10" height="11"/><rect x="0" y="15" width="16" height="2"/><path d="M28 6l10-5 10 5-10 5z"/><path d="M32 9v5c3 2 9 2 12 0V9l-6 3z"/><rect x="64" y="3" width="9" height="13" rx="1"/><path d="M88 7h5l7-5v14l-7-5h-5z"/><path d="M103 5q3 4 0 8" stroke="#f7941d" fill="none" stroke-width="1.5"/></g></svg>
        Other offerings
      </div>
    </section>
  </article>

  <!-- result 2 -->
  <article class="abs card" style="top:529px">
    <div class="abs supplier-logo" style="color:#7a1a1a"><span class="dot" style="background:#7a1a1a"></span>Harlow Beans</div>
    <h3 class="abs bean-name">Coffee bean XX</h3>
    <p class="abs blend">Blend description:</p>
    <div class="abs attr" style="top:83px">Origin [xx]</div>
    <div class="abs attr" style="top:116px">Grind availability [xx]</div>
    <section class="abs reviews">
      <div class="reviews-head">
        <svg width="34" height="30" viewBox="0 0 34 30"><path d="M17 2C8 2 2 7 2 13s6 11 15 11c2 0 3 0 5-1l8 4-2-6c2-2 4-5 4-8C32 7 26 2 17 2z" fill="none" stroke="#f7941d" stroke-width="2"/></svg>
        Reviews for this bean
      </div>
      <div class="rating">
        <div class="stars">
          <svg width="116" height="22" viewBox="0 0 116 22"><use href="#s"/><use href="#s" x="23"/><use href="#s" x="46"/><path transform="translate(69 0)" fill="#d6d6d6" d="M11 1l3 7h7l-5.6 4.3 2.1 7.2L11 15.3 4.5 19.5l2.1-7.2L1 8h7z"/><path transform="translate(92 0)" fill="#d6d6d6" d="M11 1l3 7h7l-5.6 4.3 2.1 7.2L11 15.3 4.5 19.5l2.1-7.2L1 8h7z"/></svg>
        </div>
        <span>Wholesaler's overall<br>customer rating</span>
      </div>
      <div class="offerings">
        <svg class="offer-icons" width="112" height="18" viewBox="0 0 112 18"><g fill="#f7941d"><rect x="2" y="4" width="10" height="11"/><rect x="0" y="15" width="16" height="2"/><path d="M28 6l10-5 10 5-10 5z"/><path d="M32 9v5c3 2 9 2 12 0V9l-6 3z"/><rect x="64" y="3" width="9" height="13" rx="1"/><path d="M88 7h5l7-5v14l-7-5h-5z"/><path d="M103 5q3 4 0 8" stroke="#f7941d" fill="none" stroke-width="1.5"/></g></svg>
        Other offerings
      </div>
    </section>
  </article>
</main>

<footer>
  <div class="abs footer-rule"></div>

  <div class="abs col" style="left:122px">
    <div class="col-photo" role="img" aria-label="Photo of a coffee cup on a dark background" style="background:radial-gradient(circle at 50% 60%,#bbb,#333 70%)"></div>
    <h3>Helpful Info</h3>
    <ul>
      <li><span class="caret"></span>About us</li>
      <li>Media Enquiries</li>
      <li>Terms &amp; Conditions</li>
      <li>Privacy Policy</li>
    </ul>
  </div>
  <div class="abs col-divider" style="left:387px"></div>

  <div class="abs col" style="left:453px">
    <div class="col-photo" role="img" aria-label="Portrait photo of a team member" style="background:radial-gradient(circle at 50% 40%,#999,#222 75%)"></div>
    <h3>Who We Are</h3>
    <ul>
      <li><span class="caret"></span>How It Works</li>
      <li>FAQ</li>
      <li>Contact Us</li>
    </ul>
  </div>
  <div class="abs col-divider" style="left:727px"></div>

  <div class="abs col" style="left:792px">
    <div class="col-photo" role="img" aria-label="Photo of a white cup filled with coffee beans" style="background:linear-gradient(#3a2a20 35%,#eee 36%,#fff)"></div>
    <h3>Join Us On</h3>
    <ul class="social" style="width:136px">
      <li><span class="icon"></span>Friendwall</li>
      <li><span class="icon"></span>Chirper</li>
      <li><span class="icon"></span>Worklink</li>
      <li><span class="icon"></span>Viewtube</li>
    </ul>
  </div>

  <div class="abs copyright-bar"></div>
  <p class="abs copyright">Copyright © 2014 Brewline</p>
</footer>

</body>
</html>
```